Graphic design for "How It Works" for VelmoraStyles.com*

VelmoraStyles.com website is for selling custom designer outfits for women and girls in all countries, customers can choose existing designs on this website and customize to their measurements. Customers can also provide their own designs and measurements and our expert designers and tailors get the outfit stitched and delivered to the customer.

We wanted to explain how this entire process works in 4 steps in the form of graphic design with little heading and text describing each step.

Step 1: Select Dress
Its time to choose the beauty you want to adorn yourself with. We have a wide collection of premium dresses, colours and accessories. There is something for everyone! All you need to do is pick. If you can’t find what you are looking for then you can share a picture of what you want, we will get it done whatever you want.

Step 2: Customization
Everyone is different; hence we realise the need for customization of the design and size. Here you select exactly how you want your dress to be. From sleeves to cuts, everything will be done as per your wish. Enter your measurements, lo and behold! You’re done. Leave your comments for even more customization.

Step 3: Designer Consultation
We as a user-friendly brand, aspire to provide the best of services to our clients. Our expert lady designers will help you for everything right from selecting of fabric to design of dress to necessary accessories. Our designers are just a call away!

Step 4: Stitch and Deliver
After you have placed your order, we confirm and verify the details. The boutique completes your order, sends it to us and we deliver it to your doorstep. We also have a team of designers in-house to cater to your premium dressing needs.

```html
<!DOCTYPE html>
<html lang="en">
<head>
<meta charset="utf-8">
<title>How It Works – VelmoraStyles.com</title>
<link rel="stylesheet" href="https://fonts.googleapis.com/css2?family=Montserrat:wght@400;500;600;700;800&display=swap">
<style>
  :root{
    --page-bg:#d8d4d9;
    --magenta:#a63d7a;
    --magenta-deep:#93306a;
    --magenta-light:#b8508f;
    --charcoal:#4b4a4c;
    --sheet:#f0ecf3;
    --lavender:#c9c3e6;
    --lavender-deep:#a89fd6;
    --coral:#e0463f;
    --white:#ffffff;
    --ink:#2e2d31;
  }
  *{box-sizing:border-box;margin:0;padding:0}
  html,body{width:1200px;height:800px;overflow:hidden}
  body{
    background:var(--page-bg);
    font-family:"Montserrat",sans-serif;
    display:flex;align-items:center;justify-content:center;
  }
  .flyer{
    width:560px;height:784px;
    background:var(--sheet);
    display:flex;flex-direction:column;
    box-shadow:0 2px 10px rgba(0,0,0,.15);
  }
  .flyer__header{
    height:92px;
    background:linear-gradient(90deg,var(--magenta-light),var(--magenta-deep));
    display:flex;align-items:center;justify-content:center;
  }
  .flyer__title{
    color:#f6e9f1;
    font-weight:800;
    font-size:44px;
    letter-spacing:1.5px;
  }
  .flyer__body{
    flex:1;
    margin:12px 12px 0;
    border:2px dotted var(--magenta);
    border-bottom:none;
    display:grid;
    grid-template-columns:1fr 1fr;
    grid-template-rows:repeat(4,1fr);
  }
  .step{
    padding:16px 16px 10px;
    color:var(--white);
    display:flex;flex-direction:column;justify-content:center;
  }
  .step--dark{background:var(--charcoal)}
  .step--pink{background:var(--magenta)}
  .step__label{
    font-weight:700;font-size:12.5px;letter-spacing:.5px;
  }
  .step__name{
    font-weight:700;font-size:12.5px;letter-spacing:.5px;
    margin-bottom:4px;
  }
  .step__text{
    font-size:8.6px;line-height:1.42;
    text-align:justify;
  }
  .scene{
    display:flex;flex-direction:column;align-items:center;justify-content:center;
    padding:12px 16px 8px;
  }
  .scene__art{
    width:88%;height:108px;
    border-radius:12px;
    background:linear-gradient(135deg,var(--lavender),var(--lavender-deep));
    border:4px solid #9c93cc;
  }
  .scene__caption{
    margin-top:7px;
    font-size:11px;font-weight:500;color:var(--ink);
  }
  .flyer__footer{
    height:58px;
    background:var(--charcoal);
    display:flex;align-items:center;justify-content:center;
  }
  .flyer__url{
    color:#ebe7ee;
    font-size:18px;font-weight:500;
    letter-spacing:4px;
  }
</style>
</head>
<body>
  <main class="flyer">
    <header class="flyer__header">
      <h1 class="flyer__title">HOW IT WORKS</h1>
    </header>

    <section class="flyer__body">
      <figure class="scene">
        <div class="scene__art" role="img" aria-label="Illustration of an online shop window showing a red dress with colour choices and a cart button"></div>
        <figcaption class="scene__caption">Select Dress</figcaption>
      </figure>
      <article class="step step--dark">
        <h2 class="step__label">STEP 1:</h2>
        <h3 class="step__name">SELECT DRESS</h3>
        <p class="step__text">Its time to choose the beauty you want to adorn yourself with. We have a wide collection of premium dresses, colours and accessories. There is something for everyone! All you need to do is pick. If you can’t find what you are looking for then you can share a picture of what you want, we will get it done whatever you want.</p>
      </article>

      <article class="step step--pink">
        <h2 class="step__label">STEP 2:</h2>
        <h3 class="step__name">CUSTOMIZATION</h3>
        <p class="step__text">Everyone is different; hence we realise the need for customization of the design and size. Here you select exactly how you want your dress to be. From sleeves to cuts, everything will be done as per your wish. Enter your measurements, lo and behold! You’re done. Leave your comments for even more customization.</p>
      </article>
      <figure class="scene">
        <div class="scene__art" role="img" aria-label="Illustration of a woman with a phone beside a browser window of red dress options"></div>
        <figcaption class="scene__caption">Customization</figcaption>
      </figure>

      <figure class="scene">
        <div class="scene__art" role="img" aria-label="Illustration of a customer and a designer seated in armchairs discussing dresses on a screen"></div>
        <figcaption class="scene__caption">Designer Consultation</figcaption>
      </figure>
      <article class="step step--dark">
        <h2 class="step__label">STEP 3:</h2>
        <h3 class="step__name">DESIGNER CONSULTATION</h3>
        <p class="step__text">We as a user-friendly brand, aspire to provide the best of services to our clients. Our expert lady designers will help you for everything right from selecting of fabric to design of dress to necessary accessories. Our designers are just a call away!</p>
      </article>

      <article class="step step--pink">
        <h2 class="step__label">STEP 4:</h2>
        <h3 class="step__name">STITCH AND DELIVER</h3>
        <p class="step__text">After you have placed your order, we confirm and verify the details. The boutique completes your order, sends it to us and we deliver it to your doorstep. We also have a team of designers in-house to cater to your premium dressing needs.</p>
      </article>
      <figure class="scene">
        <div class="scene__art" role="img" aria-label="Illustration of a tailor at a sewing machine and a courier handing a parcel to a woman in a red dress"></div>
        <figcaption class="scene__caption">Stitch and Deliver</figcaption>
      </figure>
    </section>

    <footer class="flyer__footer">
      <p class="flyer__url">www.velmorastyles.com</p>
    </footer>
  </main>
</body>
</html>
```